Post Card (5x7) - Pre-foreclosure Image - Harbor Path Partners

(Two-Sided Post Card)
FACING FORECLOSURE? YOU STILL HAVE OPTIONS.
If you’re behind on payments or at risk of foreclosure, you’re not alone—and it’s not too late to take action.
We help homeowners:
• Explore options to stay in their home
• Stop or delay foreclosure
• Sell quickly for a fair price if needed
No pressure. No obligation. Just real solutions tailored to your situation.
Call - (240) 558-2094
Email - marcus@hpbllc-mail.com
Harbor Path Partners LLC
7200 Bramwick Lane, Ellicott City, MD 21043
**Marcus Fennimore is a Licensed Realtor with Copperleaf Homes Realty in Bethesda, Maryland.
(Leave room for mailing address, return address & postage)
Target Market(s)
Distressed Homeowners
Industry/Entity Type
Real Estate

```html
<!DOCTYPE html>
<html lang="en">
<head>
<meta charset="UTF-8">
<title>Harbor Path Partners – Pre-foreclosure Postcard</title>
<link href="https://fonts.googleapis.com/css2?family=Poppins:wght@400;500;600;700;800&display=swap" rel="stylesheet">
<style>
  :root {
    --navy: #0a1724;
    --orange: #f2902b;
    --white: #ffffff;
    --sky-top: #6f6a5e;
    --sky-mid: #c98a3a;
    --sun: #f7b54a;
    --water: #2a1c10;
  }
  * { margin: 0; padding: 0; box-sizing: border-box; }
  html, body { width: 1200px; height: 862px; overflow: hidden; background: #e6e7e9; }
  body { font-family: "Poppins", sans-serif; }
  .postcard {
    position: relative;
    width: 1200px;
    height: 862px;
    background: var(--navy);
    overflow: hidden;
    color: var(--white);
  }
  .postcard__art { position: absolute; inset: 0; }
  .brand {
    position: absolute;
    left: 88px;
    top: 112px;
    width: 200px;
    text-align: center;
    font-weight: 500;
    font-size: 22px;
    letter-spacing: 4px;
    line-height: 1.25;
    color: var(--white);
  }
  .headline {
    position: absolute;
    left: 86px;
    top: 236px;
    font-weight: 800;
    font-size: 64px;
    line-height: 67px;
    letter-spacing: 0.5px;
  }
  .headline__accent { color: var(--orange); }
  .subhead {
    position: absolute;
    left: 88px;
    top: 386px;
    font-weight: 600;
    font-size: 29px;
    letter-spacing: 0.2px;
  }
  .subhead span { color: var(--orange); }
  .rule {
    position: absolute;
    left: 88px;
    top: 438px;
    width: 69px;
    height: 4px;
    background: var(--orange);
  }
  .intro {
    position: absolute;
    left: 88px;
    top: 455px;
    width: 460px;
    font-size: 17px;
    line-height: 25px;
  }
  .intro strong { color: var(--orange); font-weight: 600; }
  .benefit {
    position: absolute;
    top: 568px;
    width: 190px;
    margin-left: -95px;
    text-align: center;
  }
  .benefit__icon { width: 76px; height: 76px; display: block; margin: 0 auto 12px; }
  .benefit__title { color: var(--orange); font-weight: 700; font-size: 14.5px; line-height: 18px; }
  .benefit__text { font-size: 14px; line-height: 16px; }
  .divider { position: absolute; top: 567px; width: 2px; height: 148px; background: var(--white); }
  .promise {
    position: absolute;
    left: 168px;
    top: 766px;
    color: var(--navy);
    font-size: 20px;
    line-height: 27px;
  }
  .promise strong { font-weight: 700; display: block; }
  .promise__icon { position: absolute; left: 86px; top: 768px; width: 56px; height: 62px; }
</style>
</head>
<body>
<div class="postcard">
  <svg class="postcard__art" width="1200" height="862" viewBox="0 0 1200 862">
    <defs>
      <linearGradient id="skyline" x1="0" y1="0" x2="0" y2="1">
        <stop offset="0" stop-color="var(--sky-top)"/>
        <stop offset="0.35" stop-color="var(--sky-mid)"/>
        <stop offset="0.5" stop-color="var(--sun)"/>
        <stop offset="0.62" stop-color="#3a2612"/>
        <stop offset="0.78" stop-color="#a8651c"/>
        <stop offset="1" stop-color="var(--water)"/>
      </linearGradient>
    </defs>
    <polygon points="503,0 1200,0 1200,862 914,862" fill="url(#skyline)" role="img" aria-label="City skyline silhouetted at sunset over a river"/>
    <polygon points="0,735 760,735 705,862 0,862" fill="var(--orange)"/>
  </svg>

  <div class="brand">HARBOR PATH<br>PARTNERS LLC</div>

  <h1 class="headline">FACING<br><span class="headline__accent">FORECLOSURE?</span></h1>
  <p class="subhead">YOU STILL HAVE <span>OPTIONS.</span></p>
  <div class="rule"></div>
  <p class="intro">If you’re behind on payments or at risk of foreclosure, you’re not alone—and <strong>it’s not too late to take action.</strong></p>

  <div class="benefit" style="left:156px">
    <svg class="benefit__icon" viewBox="0 0 76 76" fill="none" stroke="#fff" stroke-width="2">
      <circle cx="38" cy="38" r="36"/>
      <path d="M20 38 L38 22 L56 38 M25 34 V54 H34 V43 H42 V54 H51 V34 M25 30 V22 H29 V26" stroke-linejoin="round"/>
    </svg>
    <div class="benefit__title">EXPLORE OPTIONS</div>
    <div class="benefit__text">to stay in<br>your home</div>
  </div>
  <div class="divider" style="left:258px"></div>
  <div class="benefit" style="left:359px">
    <svg class="benefit__icon" viewBox="0 0 76 76" fill="none" stroke="#fff" stroke-width="2">
      <circle cx="38" cy="38" r="36"/>
      <path d="M50 34 A15 15 0 1 0 36 51"/>
      <path d="M35 27 V37 L30 42"/>
      <path d="M47 40 L57 56 H37 Z" fill="#fff"/>
      <path d="M47 45 V50 M47 52 V53.5" stroke="var(--navy)"/>
    </svg>
    <div class="benefit__title">STOP OR DELAY</div>
    <div class="benefit__text">foreclosure</div>
  </div>
  <div class="divider" style="left:461px"></div>
  <div class="benefit" style="left:563px">
    <svg class="benefit__icon" viewBox="0 0 76 76" fill="none" stroke="#fff" stroke-width="2" stroke-linejoin="round">
      <circle cx="38" cy="38" r="36"/>
      <path d="M14 34 L21 30 L27 44 L20 47 Z M62 34 L55 30 L49 44 L56 47 Z"/>
      <path d="M24 33 L33 30 L44 36 L41 39 L34 35 M52 33 L43 30 M27 43 L37 52 L46 44 L49 43"/>
      <path d="M32 46 L36 50 M36 43 L41 48 M40 41 L44 45"/>
      <path d="M38 15 V21 M29 18 L31 23 M47 18 L45 23"/>
    </svg>
    <div class="benefit__title">SELL QUICKLY</div>
    <div class="benefit__text">for a fair price<br>if needed</div>
  </div>

  <svg class="promise__icon" viewBox="0 0 56 62" fill="none" stroke="var(--navy)" stroke-width="5" stroke-linejoin="round" stroke-linecap="round">
    <path d="M28 4 L51 12 V30 C51 44 40 54 28 58 C16 54 5 44 5 30 V12 Z"/>
    <path d="M17 31 L25 39 L40 23"/>
  </svg>
  <p class="promise"><strong>No pressure. No obligation.</strong>Just real solutions tailored to your situation.</p>
</div>
</body>
</html>
```